Larkmoor Apartments Downtown Northport

We are looking to redesign our entry way sign at Larkmoor Apartments, a low density residential apartment building, located in Downtown Northport, Alabama, U.S. Downtown Northport is a bustling boutique business district with a small town feel comprised of shops, restaurants, and a renowned arts community known for Velloway Arts Center and Festival which is one of the nation's top outdoor arts festivals. Larkmoor Apartments and its sign is the first thing you seen when you enter Downtown Northport. We are looking to redesign our sign, entry way and landscaping to compliment the building and character of the historic downtown.

Target Market(s)

Our apartment building is comprised of 20 apartments units with tenants who are primarily part of the local workforce, young professionals, or students at the Tressdale University or other nearby institutions.

Requirements
Must have
• The name of the apartment building - Larkmoor
Phone number on the sign 205-555-0148

```html
<!DOCTYPE html>
<html lang="en">
<head>
<meta charset="utf-8">
<title>Larkmoor Apartments Entry Sign</title>
<link rel="stylesheet" href="https://fonts.googleapis.com/css2?family=Arvo:wght@700&family=Fira+Sans:wght@600&display=swap">
<style>
  :root {
    --page-bg: #ebe8e3;
    --sign-red: #b94c51;
    --band-red: #9a3035;
    --wave-white: #d9d6d6;
    --type-white: #ece9e8;
  }
  html, body {
    margin: 0;
    padding: 0;
    width: 1200px;
    height: 1200px;
    overflow: hidden;
    background: var(--page-bg);
  }
  .canvas {
    position: relative;
    width: 1200px;
    height: 1200px;
  }
  .entry-sign {
    position: absolute;
    left: 40px;
    top: 230px;
    width: 1120px;
    height: 740px;
    display: block;
  }
  .sign-field { fill: var(--sign-red); }
  .accent-band { fill: var(--band-red); }
  .accent-wave { fill: var(--wave-white); }
  .building-name {
    font-family: "Arvo", "Rockwell", serif;
    font-weight: 700;
    font-size: 126px;
    fill: var(--type-white);
  }
  .phone-number {
    font-family: "Fira Sans", "Helvetica Neue", sans-serif;
    font-weight: 600;
    font-size: 56px;
    fill: var(--type-white);
    letter-spacing: -1px;
  }
</style>
</head>
<body>
<main class="canvas">
  <svg class="entry-sign" viewBox="0 0 1120 740" xmlns="http://www.w3.org/2000/svg" aria-label="Larkmoor entry sign">
    <rect class="sign-field" x="0" y="0" width="1120" height="740"/>
    <path class="accent-wave" d="M112,0 C40,90 20,220 80,380 C140,530 120,640 30,740 L112,740 Z"/>
    <rect class="accent-band" x="112" y="0" width="84" height="740"/>
    <rect class="accent-band" x="112" y="481" width="1008" height="104"/>
    <path class="accent-wave" d="M196,481 C300,420 450,395 600,405 C720,413 760,440 900,430 C1000,422 1070,392 1120,365 L1120,481 Z"/>
    <text class="building-name" x="240" y="340" textLength="810" lengthAdjust="spacingAndGlyphs">LARKMOOR</text>
    <text class="phone-number" x="1050" y="648" text-anchor="end">205-555-0148</text>
  </svg>
</main>
</body>
</html>
```